I already have a logo created by Quillory Makers that I'm very happy with. I need to spruce up my business card now. Its a double sided card with not much info on it, I like to keep it simple.
Front of card: name, phone # email address, web address. Tag Line "Outsourced Technology Solutions", under that it says Business Voice Services & Electronic Protection.
Rear of Card: Content written inside a "cloud" saying "Cloud Solutions" "Cloud Integrity"

Target Market(s)

Business to Business

Industry/Entity Type

Business

Contact Information for Business Card

We are in the technology field. Providing Telephone systems (hardware), SIP Trunks (dial tone/local/long distance/telephone #'s), LAN (Local Area Network)infrastructure cabling, Data Center solutions and Security Applications (Camera systems, Access Control systems,

Requirements
Must have
• Must have brevity
Should not have
• Clutter and/or too much information

```html
<!DOCTYPE html>
<html lang="en">
<head>
<meta charset="utf-8">
<title>Northvale Linkworks – Business Card</title>
<link rel="stylesheet" href="https://fonts.googleapis.com/css2?family=Montserrat:ital,wght@0,300;0,400;0,500;0,600;1,500&display=swap">
<style>
  :root {
    --page-bg: #3a3b3d;
    --brand-blue: #1d4a9c;
    --brand-blue-deep: #0f2f72;
    --brand-blue-light: #2f63bf;
    --paper: #ffffff;
    --band-grey: #8d8f92;
    --band-grey-light: #b9babc;
    --text-grey: #6f7275;
    --text-dark: #4a4c4f;
    --text-light: #ffffff;
  }
  * { box-sizing: border-box; margin: 0; padding: 0; }
  html, body {
    width: 1200px; height: 843px; overflow: hidden;
    background: var(--page-bg);
    font-family: "Montserrat", Arial, sans-serif;
  }
  .canvas {
    width: 1200px; height: 843px;
    display: flex; flex-direction: column;
    align-items: center; justify-content: center; gap: 36px;
  }
  .card {
    position: relative;
    width: 640px; height: 366px;
    overflow: hidden;
  }

  /* Rear side */
  .card-back {
    background: linear-gradient(135deg, var(--brand-blue-light) 0%, var(--brand-blue) 45%, var(--brand-blue-deep) 100%);
    color: var(--text-light);
    display: flex; flex-direction: column;
    align-items: center; justify-content: center;
  }
  .brand { display: flex; align-items: center; gap: 14px; }
  .brand-dot { width: 20px; height: 20px; border-radius: 50%; }
  .card-back .brand-dot { background: var(--text-light); }
  .brand-name { font-weight: 600; font-size: 30px; line-height: 1.05; letter-spacing: 0.2px; }
  .card-back .tagline {
    margin-top: 8px; padding-top: 6px;
    border-top: 1px solid rgba(255,255,255,0.6);
    font-weight: 300; font-size: 16px; color: #dfe6f4;
  }
  .cloud-lines {
    margin-top: 40px;
    font-weight: 500; font-size: 21px; letter-spacing: 0.5px;
  }
  .cloud-lines span + span::before { content: "  |  "; white-space: pre; opacity: 0.7; }

  /* Front side */
  .card-front { background: var(--brand-blue); }
  .card-front .shapes { position: absolute; inset: 0; }
  .front-brand {
    position: absolute; left: 190px; top: 50px;
    color: var(--brand-blue);
  }
  .front-brand .brand-dot { background: var(--brand-blue); }
  .front-brand .brand-name { font-size: 27px; }
  .front-brand .tagline {
    margin-top: 6px; padding-top: 5px; margin-left: 34px;
    border-top: 1px solid var(--band-grey-light);
    font-weight: 300; font-size: 15px; color: var(--text-grey);
  }
  .services {
    margin-top: 4px; margin-left: 34px;
    font-style: italic; font-weight: 500; font-size: 14px; color: var(--text-dark);
  }
  .contact-list {
    position: absolute; left: 30px; top: 188px;
    list-style: none; color: var(--text-light);
    font-size: 14px; font-weight: 400;
  }
  .contact-list li { display: flex; align-items: center; gap: 10px; height: 24px; }
  .contact-list svg { width: 15px; height: 15px; fill: var(--text-light); }
  .person {
    position: absolute; right: 34px; bottom: 30px;
    text-align: right; color: var(--text-light);
  }
  .person-name { font-weight: 600; font-size: 22px; letter-spacing: 0.4px; }
  .person-title { font-weight: 400; font-size: 16px; margin-top: 2px; }
</style>
</head>
<body>
<main class="canvas">

  <section class="card card-back" aria-label="Card rear side">
    <div class="brand">
      <span class="brand-dot"></span>
      <span class="brand-name">Northvale<br>Linkworks, LLC</span>
    </div>
    <p class="tagline">Outsourced Technology Solutions</p>
    <p class="cloud-lines"><span>Cloud Solutions</span><span>Cloud Integrity</span></p>
  </section>

  <section class="card card-front" aria-label="Card front side">
    <svg class="shapes" viewBox="0 0 640 366" preserveAspectRatio="none" aria-hidden="true">
      <defs>
        <linearGradient id="greyBand" x1="0" y1="0" x2="1" y2="1">
          <stop offset="0" stop-color="#a9abae"/>
          <stop offset="1" stop-color="#7c7e81"/>
        </linearGradient>
        <linearGradient id="blueField" x1="0" y1="0" x2="1" y2="1">
          <stop offset="0" stop-color="#2a5bb5"/>
          <stop offset="1" stop-color="#0f2f72"/>
        </linearGradient>
      </defs>
      <rect width="640" height="366" fill="url(#blueField)"/>
      <polygon points="540,0 640,0 640,268 0,150 0,0" fill="url(#greyBand)"/>
      <polygon points="0,0 570,0 618,258 0,146" fill="#ffffff"/>
    </svg>

    <div class="front-brand">
      <div class="brand">
        <span class="brand-dot"></span>
        <span class="brand-name">Northvale<br>Linkworks, LLC</span>
      </div>
      <p class="tagline">Outsourced Technology Solutions</p>
      <p class="services">Business Voice Services &amp; Electronic Protection</p>
    </div>

    <ul class="contact-list">
      <li>
        <svg viewBox="0 0 24 24" aria-hidden="true"><path d="M6.6 10.8a15.1 15.1 0 0 0 6.6 6.6l2.2-2.2a1 1 0 0 1 1-.25 11.4 11.4 0 0 0 3.6.57 1 1 0 0 1 1 1V20a1 1 0 0 1-1 1A17 17 0 0 1 3 4a1 1 0 0 1 1-1h3.5a1 1 0 0 1 1 1c0 1.25.2 2.45.57 3.57a1 1 0 0 1-.25 1z"/></svg>
        <span>555 0142 7781</span>
      </li>
      <li>
        <svg viewBox="0 0 24 24" aria-hidden="true"><path d="M2 5h20v14H2zm2 2v.5l8 5 8-5V7zm0 2.9V17h16V9.9l-8 5z"/></svg>
        <span>marcus@northvale.example</span>
      </li>
      <li>
        <svg viewBox="0 0 24 24" aria-hidden="true"><circle cx="12" cy="12" r="10"/><path d="M2 12h20M12 2c3 3 3 17 0 20M12 2c-3 3-3 17 0 20" stroke="#1d4a9c" stroke-width="1.6" fill="none"/></svg>
        <span>www.northvale.example</span>
      </li>
    </ul>

    <div class="person">
      <p class="person-name">Marcus Hale</p>
      <p class="person-title">President</p>
    </div>
  </section>

</main>
</body>
</html>
```